Poster Design Project

We are youth orchestra in Texas that is introducing a new summer program called: Riverbend Bow Academy (It's for students ages 8-18 who play already play violin/viola/cello/bass

Poster size: 11" by 17"

All the details are below, but on the poster we would need the website listed: www.marlowvalleyensemble.example and tell them to go to that website to apply online beginning April 1st

That's how we get business, they go to our website and apply. It also needs to say really big MVE RIVERBEND BOW ACADEMY

We want to use these posters every summer so no dates on it please. Only: April 1st is when we being accepting online applications (every year, so don't put a year) Also put: Camp is held on Saturdays in June and July with final concert, last Sunday in July

Also on the poster we need: Our goal is to keep young musicians playing over the summer –so don’t put your instrument away for the summer! Keep in shape by joining us for the Marlow Valley Ensemble’s summer program – Riverbend Bow Academy! Tuition is $225, which covers June/July Saturday rehearsals and the performance fee for the HPSD Hall concert, last Sunday in July.

I know we can't get all the info below on it, but I put it on so you could better understand what we are doing.

We have a logo already, that we have the rights to - I need something that kids/teens will think is cool looking and music related....we are string instruments only (violin, viola, cello, bass) we also want it to look classy looking, not cheap
I included 2 copies of the logo in different color set

here's all the details from our website:
Riverbend Bow Academy (June and July) - Tuition: $225

Rehearsals on Saturdays June &July with final concert on last Sunday in July @ HPHS Hall

Our goal is to keep young musicians playing over the summer –so don’t put your instrument away for the summer! Keep in shape by joining us for the Marlow Valley Ensemble’s new summer program – Riverbend Bow Academy!

Tuition is $225, which covers June/July Saturday rehearsals and the performance fee for the HPSD Hall concert.

No audition is necessary. Enrollment is limited to the first 50 students in each age category, depending on instrumentation needs, so don’t delay – enrollment online begins April 1st. Siblings will receive a $50 discount, after the first child's regular priced tuition.

Riverbend Bow I: Students entering grades 6 and below (3:00 – 4:20 P.M. )
Riverbend Bow II: Students grades entering 7 and 8 (4:30 – 6:00 P.M.)
Riverbend Bow III: Students entering grades 9-12 (6:15 – 7:45 P.M.)

Summer camp attendance policy is more lenient due to summer vacations. Please notify MVE of summer absences as soon as your vacation/camp dates are known.

Target Market(s)

string players ages 10-18 and their parents

Industry/Entity Type

Business

Requirements
Must have
• Be able to see title from far, and prominently display how/when to apply and where (website)

Also only the concert is at HPHS Hall, we rehearse at Fenwick Music in Allen

I'm working on uploading files for our QR codes for website and phone - It's uploaded below
Nice to have
• If you have room, the Riverbend Bow Academy I II and III times/grades, etc. but doesn't have to be seen as prominently as the title and how to apply
Should not have
• pictures of violin/vla/cello/bass students if they look elementary aged, should be more in the teenager age group if you use pictures.

```html
<!DOCTYPE html>
<html lang="en">
<head>
<meta charset="utf-8">
<title>MVE Riverbend Bow Academy</title>
<link rel="stylesheet" href="https://fonts.googleapis.com/css2?family=Encode+Sans+Condensed:wght@600;700;800&family=Source+Sans+3:ital,wght@0,400;1,400&display=swap">
<style>
  :root {
    --ink: #000000;
    --paper: #ffffff;
    --rule: #5a5a5a;
    --grad-blue: #1f8fc8;
    --grad-teal: #2fbfb0;
    --grad-lime: #c9e83a;
    --grad-yellow: #f7ec1c;
    --grad-orange: #f2a311;
    --accent-red: #b5323e;
    --accent-blue: #1d83c6;
    --wood-dark: #6e3a14;
    --wood-light: #c9732a;
    --brand: #e9eef2;
  }
  * { box-sizing: border-box; margin: 0; padding: 0; }
  html, body { width: 776px; height: 1200px; overflow: hidden; background: var(--ink); }
  .poster {
    position: relative;
    width: 776px;
    height: 1200px;
    background: var(--ink);
    color: var(--paper);
    font-family: "Source Sans 3", Arial, sans-serif;
    overflow: hidden;
  }

  /* Brand block */
  .brand {
    position: absolute;
    left: 150px;
    top: 40px;
    width: 500px;
    height: 150px;
    display: flex;
    align-items: center;
    gap: 18px;
    color: var(--brand);
    font-family: "Encode Sans Condensed", "Arial Narrow", sans-serif;
    font-weight: 700;
  }
  .brand-dot {
    width: 54px; height: 54px; border-radius: 50%;
    background: var(--grad-blue);
    flex: none;
  }
  .brand-name { font-size: 22px; line-height: 1.05; letter-spacing: 0.5px; text-transform: uppercase; }
  .brand-mark { font-size: 96px; line-height: 1; margin-left: 10px; }
  .brand-rule {
    position: absolute; left: 68px; top: 203px; width: 660px; height: 1px;
    background: linear-gradient(90deg, transparent, #8a8a8a 20%, #8a8a8a 80%, transparent);
  }

  /* Title */
  .title {
    position: absolute;
    left: 0; right: 0; top: 238px;
    text-align: center;
    font-family: "Encode Sans Condensed", "Arial Narrow", sans-serif;
    font-weight: 800;
    text-transform: uppercase;
    line-height: 1;
  }
  .title span {
    display: block;
    background: linear-gradient(90deg, var(--grad-blue) 0%, var(--grad-teal) 28%, var(--grad-lime) 50%, var(--grad-yellow) 62%, var(--grad-orange) 100%);
    -webkit-background-clip: text;
    background-clip: text;
    color: transparent;
    filter: drop-shadow(-3px 2px 0 #1a4f7a);
  }
  .title-top { font-size: 64px; letter-spacing: 0.5px; margin-left: 40px; }
  .title-main { font-size: 100px; margin-top: 8px; margin-left: 40px; }

  /* Tagline */
  .tagline {
    position: absolute;
    left: 262px; top: 530px;
    font-family: "Encode Sans Condensed", "Arial Narrow", sans-serif;
    transform: rotate(5deg);
    transform-origin: left top;
  }
  .tagline-dont { color: var(--accent-red); font-weight: 800; font-size: 32px; display: block; }
  .tagline-rest {
    color: var(--accent-blue); font-weight: 600; font-size: 38px; line-height: 0.98;
    display: block; margin-left: 62px; margin-top: -4px; text-transform: uppercase;
  }
  .tagline-rest em { font-style: normal; display: block; font-size: 46px; margin-left: -28px; }

  /* Notes */
  .notes { position: absolute; left: 0; top: 0; width: 776px; height: 820px; pointer-events: none; }

  /* Instrument illustration area */
  .instrument-art {
    position: absolute;
    left: 0; top: 478px;
    width: 168px; height: 722px;
    border-radius: 0 60px 0 0;
    background: linear-gradient(180deg, var(--wood-dark) 0%, var(--wood-light) 60%, var(--wood-dark) 100%);
    opacity: 0.85;
  }

  /* Details */
  .rules { position: absolute; left: 0; top: 0; width: 776px; height: 1200px; }
  .details { list-style: none; }
  .details li {
    position: absolute;
    font-size: 19px;
    white-space: nowrap;
    color: var(--paper);
  }
  .details .ages     { left: 202px; top: 853px; }
  .details .apply    { left: 212px; top: 892px; }
  .details .rehearse { left: 206px; top: 958px; }
  .details .concert  { left: 253px; top: 1008px; }
  .details .web      { left: 274px; top: 1058px; }
  .details .cost     { left: 264px; top: 1106px; }
  .details .cost small { font-style: italic; font-size: 15px; }
</style>
</head>
<body>
<main class="poster">

  <header class="brand" aria-label="Marlow Valley Ensemble">
    <span class="brand-dot"></span>
    <span class="brand-name">Marlow Valley<br>Ensemble</span>
    <span class="brand-mark">MVE</span>
  </header>
  <div class="brand-rule"></div>

  <h1 class="title">
    <span class="title-top">MVE Riverbend Bow</span>
    <span class="title-main">Academy</span>
  </h1>

  <p class="tagline">
    <span class="tagline-dont">DON'T</span>
    <span class="tagline-rest">Put your instrument<em>down in summer!</em></span>
  </p>

  <svg class="notes" viewBox="0 0 776 820" aria-hidden="true">
    <defs>
      <g id="note" fill="#ffffff">
        <ellipse cx="4" cy="24" rx="5" ry="3.6" transform="rotate(-20 4 24)"/>
        <ellipse cx="18" cy="20" rx="5" ry="3.6" transform="rotate(-20 18 20)"/>
        <rect x="8" y="2" width="1.8" height="22"/>
        <rect x="22" y="-2" width="1.8" height="22"/>
        <polygon points="8,2 23.8,-2 23.8,2 8,6"/>
        <polygon points="8,8 23.8,4 23.8,8 8,12"/>
      </g>
    </defs>
    <use href="#note" x="400" y="540"/>
    <use href="#note" x="460" y="570"/>
    <use href="#note" x="512" y="558"/>
    <use href="#note" x="592" y="570" transform="rotate(15 604 580)"/>
    <use href="#note" x="672" y="584"/>
    <use href="#note" x="720" y="570"/>
    <use href="#note" x="758" y="604" transform="rotate(20 770 614)"/>
    <use href="#note" x="128" y="710"/>
    <use href="#note" x="190" y="736"/>
    <use href="#note" x="236" y="722"/>
    <use href="#note" x="318" y="736" transform="rotate(15 330 746)"/>
    <use href="#note" x="398" y="752"/>
    <use href="#note" x="450" y="732"/>
    <use href="#note" x="482" y="776" transform="rotate(20 494 786)"/>
  </svg>

  <div class="instrument-art" role="img" aria-label="Stylised outline illustration of a violin in warm brown and orange, drawn vertically along the left edge"></div>

  <svg class="rules" viewBox="0 0 776 1200" aria-hidden="true">
    <g stroke="var(--rule)" stroke-width="1" fill="none">
      <line x1="150" y1="934" x2="770" y2="934"/>
      <line x1="158" y1="983" x2="770" y2="983"/>
      <line x1="178" y1="1032" x2="770" y2="1032"/>
      <line x1="178" y1="1080" x2="770" y2="1080"/>
      <line x1="150" y1="1129" x2="770" y2="1129"/>
      <line x1="770" y1="934" x2="770" y2="1129"/>
    </g>
  </svg>

  <ul class="details">
    <li class="ages">Ages: 8-18 Violin, Viola, Cello and Bass players</li>
    <li class="apply">Online applications start April 1st</li>
    <li class="rehearse">Rehearsals start: Saturdays in June/July</li>
    <li class="concert">Final Concert: Last Sunday in July</li>
    <li class="web">www.marlowvalleyensemble.example</li>
    <li class="cost">Cost: $225 <small>(Covers June/July rehearsals and final concert)</small></li>
  </ul>

</main>
</body>
</html>
```